Gazebrix fresh re-design

We are UK based company and have Magento website which we are happy with, but we require fresh design. Menu must be customer friendly

Design must reflect in strength as strength of our products and value for money are our selling points.

Our products are not family products there mainly used for business at events, cycling, running clubs, etc

New design must have same information as current design

links that require new design

http://www.gazebrix.example (landing page)

http://www.gazebrix.example/3m-x-3m-heavy-duty-tents/3m-x-3m-pop-up-marquee-white.html (product page)

http://www.gazebrix.example/custom-design-own-tent-size/choose-3mx3m.html (design tool)

Target Market(s)

business owners, cycling clubs, running clubs,

Industry/Entity Type

It Company

Number of Pages Required

3 page

Requirements
Must have
• background image of working gazebrix, clean fresh design, printed gazebrixes eg. cupcake
Should not have
• all same functions as current page

```html
<!DOCTYPE html>
<html lang="en">
<head>
<meta charset="utf-8">
<title>Gazebrix – Pop Up Gazebos</title>
<link rel="stylesheet" href="https://fonts.googleapis.com/css2?family=Questrial&family=Open+Sans:wght@400;600;700;800&family=Raleway:wght@400;500&display=swap">
<style>
:root{
  --red:#ff0000;
  --blue:#0a3a9e;
  --ink:#333333;
  --muted:#7a7a7a;
  --light:#f4f4f4;
  --panel:#ebebeb;
  --gray-btn:#555555;
  --circle:#6d6d6d;
  --footer-bar:#6e6e6e;
  --white:#ffffff;
  --line:#dddddd;
}
*{box-sizing:border-box;margin:0;padding:0}
html,body{width:1200px;height:2632px;overflow:hidden;background:var(--white)}
body{position:relative;font-family:"Open Sans",Arial,sans-serif;color:var(--ink)}
.abs{position:absolute}

/* top bar */
.topbar{left:0;top:0;width:1200px;height:47px;border-bottom:1px solid var(--line);font-size:13px;color:var(--muted)}
.topbar .phone{left:56px;top:14px;display:flex;align-items:center;gap:10px;font-size:15px;color:var(--ink)}
.topbar .prefs{left:732px;top:16px;font-size:11px;display:flex;gap:22px}
.topbar .account{left:884px;top:15px;font-size:11px;display:flex;gap:10px}
.topbar .account .login{color:var(--red)}

/* header */
.header{left:0;top:47px;width:1200px;height:137px;border-bottom:1px solid var(--line)}
.round-btn{width:78px;height:78px;border-radius:50%;background:var(--circle);display:flex;align-items:center;justify-content:center}
.search-btn{left:49px;top:30px}
.cart-btn{left:1070px;top:30px}
.cart-count{left:1124px;top:71px;width:26px;height:26px;border-radius:50%;background:var(--red);color:var(--white);font-size:12px;display:flex;align-items:center;justify-content:center}
.brand{left:0;width:1200px;top:42px;text-align:center;font-family:"Questrial",sans-serif;font-size:50px;color:var(--blue);letter-spacing:1px}

/* nav */
.nav{left:0;top:184px;width:1200px;height:67px;display:flex;justify-content:center;align-items:center;font-family:"Questrial",sans-serif;font-size:13px;letter-spacing:.5px}
.nav span{padding:0 27px}

/* hero */
.hero{left:0;top:251px;width:1200px;height:596px;background:linear-gradient(180deg,#3c4a34 0%,#2d3a27 45%,#6f8048 70%,#5e7a3a 100%)}
.hero-tent{left:215px;top:251px;width:705px;height:596px;background:linear-gradient(180deg,#f4f4f4 0%,#e6e6e6 25%,#b8b8b8 40%,#9a9a9a 100%)}
.hero-card{left:379px;top:463px;width:412px;height:358px;background:var(--light);padding:14px}
.hero-card .inner{width:100%;height:100%;background:#777777;text-align:center;padding-top:50px}
.hero-card .kicker{font-family:"Questrial",sans-serif;font-size:29px;color:var(--blue);letter-spacing:1px}
.hero-card .headline{font-family:"Questrial",sans-serif;font-size:58px;color:var(--white);letter-spacing:4px;line-height:1.1}
.hero-card p{font-size:11.5px;color:#eeeeee;padding:14px 28px 0;line-height:1.5}
.btn-red{background:var(--red);color:var(--white);font-size:13px;display:inline-flex;align-items:center;justify-content:center}
.hero-card .btn-red{width:162px;height:46px;margin-top:20px}
.dots{left:86px;top:742px;display:flex;gap:12px}
.dots i{width:18px;height:18px;border-radius:50%;background:#9a9a9a;display:block}
.dots i.on{background:var(--red)}

/* promos */
.promo{top:872px;height:305px}
.promo-left{left:49px;width:539px;background:linear-gradient(180deg,#1e4fc4 0%,#1440a8 45%,#bfc4cc 100%)}
.promo-left .btn-red{position:absolute;left:168px;top:138px;width:160px;height:44px;font-size:14px}
.promo-right{left:616px;width:536px;background:linear-gradient(180deg,#2d2f2a 0%,#1c1e1a 60%,#3d4a2f 100%);text-align:center;color:var(--white);font-family:"Questrial",sans-serif}
.promo-right .t{font-size:46px;line-height:1.2;padding-top:46px;letter-spacing:1px}
.promo-right .pct{font-family:"Open Sans",sans-serif;font-weight:700;font-size:40px;color:var(--red);line-height:1.1}
.promo-right .btn-blue{display:inline-flex;width:162px;height:44px;align-items:center;justify-content:center;background:var(--blue);font-family:"Open Sans",sans-serif;font-size:14px;margin-top:10px}

/* products */
.products{left:0;top:1207px;width:1200px;height:568px;background:var(--light)}
.section-title{left:49px;top:1245px;width:891px;display:flex;align-items:center;gap:20px;font-family:"Questrial",sans-serif;font-size:22px}
.section-title .rule{flex:1;height:1px;background:var(--line)}
.section-title .rule.short{flex:0 0 238px}
.section-title b{font-weight:400;color:var(--red)}
.filters{left:962px;top:1244px;font-size:10px;display:flex;gap:20px;color:var(--muted)}
.filters .on{color:var(--red)}
.card{top:1307px;width:271px;height:438px;border-left:1px solid var(--line);padding:0 14px}
.card.active{background:#dcdcdc}
.card .pic{height:177px;margin-top:28px}
.badge{top:1307px;width:30px;height:14px;background:var(--red);color:var(--white);font-size:9px;text-align:center;line-height:14px}
.card .row{display:flex;justify-content:space-between;align-items:center;margin-top:16px;padding-bottom:14px;border-bottom:1px solid var(--line)}
.card .price{color:var(--red);font-size:20px}
.card .qty{font-size:11px;color:var(--muted);display:flex;align-items:center;gap:8px}
.card .qty span{border:1px solid var(--line);background:var(--white);width:28px;height:24px;display:flex;align-items:center;justify-content:center;color:var(--ink)}
.card h3{font-weight:400;font-size:16px;margin-top:16px;color:#555}
.card p{font-size:11px;line-height:1.55;color:var(--muted);margin-top:6px}
.card .actions{display:flex;gap:12px;margin-top:14px}
.card .actions div{width:130px;height:48px;display:flex;align-items:center;justify-content:center;gap:8px;font-size:11px;font-weight:600;color:var(--white)}
.card .add{background:var(--red)}
.card .more{background:var(--gray-btn)}
.quick{left:385px;top:1405px;width:126px;height:44px;background:#222;color:var(--white);font-size:12px;display:flex;align-items:center;justify-content:center;gap:10px}
.stars{left:520px;top:1312px;color:#cc2222;font-size:10px;letter-spacing:1px}

/* features */
.features{left:49px;top:1775px;width:1103px;height:211px;display:flex}
.feature{flex:1;border-left:1px solid var(--line);display:flex;flex-direction:column;align-items:center;margin:30px 0;padding-top:10px}
.feature:first-child{border-left:none}
.feature .ic{width:62px;height:62px;border-radius:50%;background:var(--circle);display:flex;align-items:center;justify-content:center}
.feature.on .ic{background:var(--red)}
.feature .lbl{font-size:15px;font-weight:600;color:#666;text-align:center;margin-top:14px;line-height:1.3}
.feature.on .lbl{color:var(--red)}

/* newsletter */
.newsletter{left:0;top:1991px;width:1200px;height:202px;background:var(--panel)}
.news-title{left:90px;top:2046px;width:390px;text-align:right;font-family:"Raleway",sans-serif;font-size:36px;color:var(--red)}
.news-copy{left:80px;top:2096px;width:400px;text-align:right;font-size:12px;line-height:1.6}
.news-input{left:517px;top:2047px;width:246px;height:40px;background:var(--white);border:1px solid var(--line);font-size:11px;color:var(--muted);padding:12px 20px}
.news-btn{left:517px;top:2101px;width:246px;height:39px;background:#333;color:var(--white);font-size:11px;display:flex;align-items:center;justify-content:center}
.guarantee{left:798px;top:2015px;width:354px;height:148px;background:var(--red);color:var(--white);display:flex;align-items:center;gap:26px;padding-left:32px;font-weight:800;font-size:31px;line-height:1.1;letter-spacing:1px}

/* footer */
.footer-col{top:2245px}
.footer-col h4{font-weight:600;font-size:16px;color:#555}
.footer-col ul{list-style:none;margin-top:50px;font-size:11px;color:var(--muted)}
.footer-col li{height:34px}
.footer-rule{left:49px;top:2285px;width:1103px;height:1px;background:var(--line)}
.footer-div{top:2285px;width:1px;height:200px;background:var(--line)}
.contact{font-size:11px;color:var(--muted);line-height:1.6}
.contact .big{font-size:21px;color:var(--ink)}
.bottom-bar{left:0;top:2535px;width:1200px;height:97px;background:var(--footer-bar)}
.copy{left:54px;top:2573px;font-size:12px;color:var(--white)}
.social{left:929px;top:2564px;display:flex;gap:12px}
.social .link{width:35px;height:35px;border:2px solid var(--red);display:flex;align-items:center;justify-content:center}
.social .link.fill{background:var(--red)}
.social .dot{width:9px;height:9px;border-radius:50%;background:var(--red)}
.social .fill .dot{background:var(--white)}
</style>
</head>
<body>

<div class="abs topbar">
  <div class="abs phone">
    <svg width="16" height="16" viewBox="0 0 24 24"><path d="M6.6 10.8a15 15 0 0 0 6.6 6.6l2.2-2.2a1 1 0 0 1 1-.3 11 11 0 0 0 3.6.6 1 1 0 0 1 1 1V20a1 1 0 0 1-1 1A17 17 0 0 1 3 4a1 1 0 0 1 1-1h3.5a1 1 0 0 1 1 1 11 11 0 0 0 .6 3.6 1 1 0 0 1-.3 1z" fill="#1a3fa0"/></svg>
    0100-555-0190
  </div>
  <div class="abs prefs"><span>Dollar ⌄</span><span>English ⌄</span></div>
  <div class="abs account"><span class="login">LOGIN/REGISTER</span><span>|</span><span>MY ACCOUNT</span><span>|</span><span>WISHLIST - 0</span></div>
</div>

<div class="abs header">
  <div class="abs round-btn search-btn">
    <svg width="30" height="30" viewBox="0 0 24 24"><circle cx="10" cy="10" r="6.5" stroke="#fff" stroke-width="2.6" fill="none"/><path d="M15 15l6 6" stroke="#fff" stroke-width="3" stroke-linecap="round"/></svg>
  </div>
  <div class="abs brand">Gazebrix</div>
  <div class="abs round-btn cart-btn">
    <svg width="30" height="30" viewBox="0 0 24 24"><path d="M2 4h3l2.5 10h11L21 7H7" stroke="#fff" stroke-width="2.4" fill="none" stroke-linejoin="round"/><circle cx="9" cy="18.5" r="1.8" fill="#fff"/><circle cx="17" cy="18.5" r="1.8" fill="#fff"/></svg>
  </div>
</div>
<div class="abs cart-count">0</div>

<nav class="abs nav">
  <span>GAZEBRIXES</span><span>ROOFS</span><span>WALLS</span><span>GAZEBO WEIGHTS</span><span>GUTTERS</span><span>SANDBAGS</span><span>TABLES</span><span>PARTS</span>
</nav>

<section class="abs hero" role="img" aria-label="Photo of a white gazebrix with side walls standing on grass in front of pine trees"></section>
<div class="abs hero-tent" role="img" aria-label="White gazebrix canopy and walls"></div>
<div class="abs hero-card">
  <div class="inner">
    <div class="kicker">NEW FRAMES AND</div>
    <div class="headline">STRONG</div>
    <p>Lorem ipsum dolor sit amet, consectetur adipiscing elit, sed do eiusmod tempor incididunt ut labore et dolore magna aliqua.</p>
    <div class="btn-red">SHOP NOW</div>
  </div>
</div>
<div class="abs dots"><i class="on"></i><i></i><i></i></div>

<div class="abs promo promo-left" role="img" aria-label="Blue gazebrix with clear window side walls">
  <div class="btn-red">SHOP NOW</div>
</div>
<div class="abs promo promo-right" role="img" aria-label="Black gazebrix in a park">
  <div class="t">EXCLUSIVE<br>OFFERS</div>
  <div class="pct">25%</div>
  <div class="btn-blue">SHOP NOW</div>
</div>

<section class="abs products"></section>
<div class="abs section-title"><span class="rule"></span><span><b>NEW</b> PRODUCT</span><span class="rule short"></span></div>
<div class="abs filters"><span class="on">PRICE</span><span>CATEGORY</span><span>BRAND</span></div>

<div class="abs card" style="left:49px">
  <div class="pic" role="img" aria-label="Pink gazebrix canopy on a lawn" style="background:linear-gradient(180deg,#d8dde6 0%,#d23a6a 30%,#e0e4ea 45%,#5f8c33 60%,#4d7a2a 100%)"></div>
  <div class="row"><span class="price">$133.1</span><span class="qty">Quantity <span>1</span></span></div>
  <h3>Name of Product</h3>
  <p>Lorem ipsum dolor sit amet, consectetur edit adipiscing elit, eiusmod tempor incididunt ut sit amets edit labore</p>
  <div class="actions"><div class="add">🛒 ADD TO CART</div><div class="more">⚙ MORE</div></div>
</div>
<div class="abs card active" style="left:326px">
  <div class="pic" role="img" aria-label="Blue gazebrix on grass" style="background:linear-gradient(180deg,#cfd3d6 0%,#cfd3d6 35%,#2c4fa0 50%,#7b8c5a 62%,#6a8a3a 100%)"></div>
  <div class="row"><span class="price">$93.0</span><span class="qty">Quantity <span>1</span></span></div>
  <h3>Name of Product</h3>
  <p>Lorem ipsum dolor sit amet, consectetur edit adipiscing elit, eiusmod tempor incididunt ut sit amets edit labore</p>
  <div class="actions"><div class="add">🛒 ADD TO CART</div><div class="more">⚙ MORE</div></div>
</div>
<div class="abs card" style="left:603px">
  <div class="pic" role="img" aria-label="Gazebo weight plate fitted to a gazebrix leg on grass" style="background:linear-gradient(180deg,#a7ad8e 0%,#6c8a3e 40%,#4f6b2e 100%)"></div>
  <div class="row"><span class="price">$68.8</span><span class="qty">Quantity <span>1</span></span></div>
  <h3>Name of Product</h3>
  <p>Lorem ipsum dolor sit amet, consectetur edit adipiscing elit, eiusmod tempor incididunt ut sit amets edit labore</p>
  <div class="actions"><div class="add">🛒 ADD TO CART</div><div class="more">⚙ MORE</div></div>
</div>
<div class="abs card" style="left:880px">
  <div class="pic" role="img" aria-label="Orange gazebrix with walls on grass" style="background:linear-gradient(180deg,#3e4a2e 0%,#f28a1a 30%,#f39a2c 65%,#6a8a3a 80%,#5d7d31 100%)"></div>
  <div class="row"><span class="price">$33.1</span><span class="qty">Quantity <span>1</span></span></div>
  <h3>Name of Product</h3>
  <p>Lorem ipsum dolor sit amet, consectetur edit adipiscing elit, eiusmod tempor incididunt ut sit amets edit labore</p>
  <div class="actions"><div class="add">🛒 ADD TO CART</div><div class="more">⚙ MORE</div></div>
</div>
<div class="abs badge" style="left:52px">25%</div>
<div class="abs badge" style="left:606px">25%</div>
<div class="abs stars">★★★★★</div>
<div class="abs quick">QUICK VIEW <span>›</span></div>

<div class="abs features">
  <div class="feature on">
    <div class="ic"><svg width="26" height="26" viewBox="0 0 24 24"><rect x="5" y="11" width="14" height="10" rx="1.5" fill="#fff"/><path d="M8 11V7a4 4 0 0 1 8 0" stroke="#fff" stroke-width="2.2" fill="none"/></svg></div>
    <div class="lbl">Secure payment</div>
  </div>
  <div class="feature">
    <div class="ic"><svg width="28" height="28" viewBox="0 0 24 24"><rect x="2" y="7" width="12" height="9" fill="#fff"/><path d="M14 10h4l3 3v3h-7z" fill="#fff"/><circle cx="6" cy="17.5" r="2" fill="#fff"/><circle cx="17" cy="17.5" r="2" fill="#fff"/></svg></div>
    <div class="lbl">Free standard<br>shipping</div>
  </div>
  <div class="feature">
    <div class="ic"><svg width="26" height="26" viewBox="0 0 24 24"><path d="M19 8a8 8 0 0 0-14 1M5 16a8 8 0 0 0 14-1" stroke="#fff" stroke-width="2.4" fill="none"/><path d="M19 3v5h-5M5 21v-5h5" stroke="#fff" stroke-width="2.4" fill="none"/></svg></div>
    <div class="lbl">7day Return</div>
  </div>
  <div class="feature">
    <div class="ic"><svg width="26" height="26" viewBox="0 0 24 24"><rect x="3" y="9" width="18" height="4" fill="#fff"/><rect x="5" y="13" width="14" height="8" fill="#fff"/><path d="M12 9v12" stroke="#6d6d6d" stroke-width="2"/><path d="M12 9c-2-4-6-4-5-1M12 9c2-4 6-4 5-1" stroke="#fff" stroke-width="1.8" fill="none"/></svg></div>
    <div class="lbl">Free gift box</div>
  </div>
  <div class="feature">
    <div class="ic"><svg width="26" height="26" viewBox="0 0 24 24"><circle cx="12" cy="8" r="4.5" fill="#fff"/><path d="M3.5 21a8.5 8.5 0 0 1 17 0z" fill="#fff"/></svg></div>
    <div class="lbl">Customer<br>Support</div>
  </div>
</div>

<section class="abs newsletter"></section>
<div class="abs news-title">Newsletter Sign Up</div>
<div class="abs news-copy">Lorem ipsum dolor sit amet conse ctetur adipisicing elit, sed do eiusmod tempor incididunt ut labore et dolore magna aliqua.</div>
<div class="abs news-input">Enter your Email Address</div>
<div class="abs news-btn">SUBSCRIBE</div>
<div class="abs guarantee">
  <svg width="54" height="54" viewBox="0 0 24 24"><rect x="2" y="10" width="4" height="11" fill="#fff"/><path d="M8 10l4-7c1.5 0 2.3 1 2 2.5L13.3 9H20a2 2 0 0 1 2 2.3l-1.3 7.5A2.5 2.5 0 0 1 18.2 21H8z" fill="#fff"/></svg>
  <div>100 %<br>GUARANTEEN</div>
</div>

<div class="abs footer-rule"></div>
<div class="abs footer-div" style="left:230px"></div>
<div class="abs footer-div" style="left:460px"></div>
<div class="abs footer-div" style="left:672px"></div>
<div class="abs footer-div" style="left:914px"></div>
<div class="abs footer-col" style="left:51px"><h4>Information</h4><ul><li>ABOUT US</li><li>DELIVERY INFORMATION</li><li>PRIVACY POLICY</li><li>TERMS &amp; CONDITIONS</li></ul></div>
<div class="abs footer-col" style="left:281px"><h4>Customer Service</h4><ul><li>CONTACT US</li><li>RETURNS</li><li>SITE MAP</li><li>FORGET PASSWORD</li></ul></div>
<div class="abs footer-col" style="left:505px"><h4>Extras</h4><ul><li>BRANDS</li><li>GIFT VOUCHERS</li><li>AFFILIATES</li><li>SPECIALS</li></ul></div>
<div class="abs footer-col" style="left:724px"><h4>My Account</h4><ul><li>MY ACCOUNT</li><li>ORDER HISTORY</li><li>WISH LIST</li><li>NEWSLETTER</li></ul></div>
<div class="abs footer-col" style="left:965px">
  <h4>Contact Us</h4>
  <div class="contact" style="margin-top:48px">MY COMPANY , ADDRESS LINE1,<br>ADDRESS LINE2, COUNTRY -123456</div>
  <div class="contact" style="margin-top:22px">CALL US NOW TOLL FREE:<br><span class="big">0100-555-0123</span></div>
  <div class="contact" style="margin-top:22px">EMAIL:<br>&nbsp;&nbsp;&nbsp;INFO@GAZEBRIX-MAIL.EXAMPLE</div>
</div>

<footer class="abs bottom-bar"></footer>
<div class="abs copy">All Right Reserved. Copyrights @2015</div>
<div class="abs social">
  <div class="link" aria-label="RSS feed">
    <svg width="17" height="17" viewBox="0 0 24 24"><circle cx="5" cy="19" r="2.5" fill="#ff0000"/><path d="M3 11a10 10 0 0 1 10 10M3 4a17 17 0 0 1 17 17" stroke="#ff0000" stroke-width="3" fill="none"/></svg>
  </div>
  <div class="link" aria-label="Social link"><span class="dot"></span></div>
  <div class="link" aria-label="Social link"><span class="dot"></span></div>
  <div class="link fill" aria-label="Social link"><span class="dot"></span></div>
  <div class="link" aria-label="Social link"><span class="dot"></span></div>
</div>

</body>
</html>
```